Webdesign für IT-Dienstleister
Zielgruppe
Seit 1997 bieten wir erstklassige IT-Dienstleistungen Mainz an, die darauf ausgerichtet sind, Unternehmen und Privatkunden mit kompetenter Beratung, zuverlässiger Unterstützung und modernen Technologielösungen zur Seite zu stehen.
Umfassende Computer-Serviceleistungen
Unser Computer-Service Mainz beinhaltet eine Reihe von Dienstleistungen, die darauf abzielen, die Leistungsfähigkeit Ihrer IT-Infrastruktur zu optimieren und zu erhalten. Von der Fehlerdiagnose bis hin zur Wartung bieten wir ein Rundum-Sorglos-Paket für Ihre Hardware und Software.
Professionelle Fehleranalyse und Reparatur
Optimierung von Betriebssystemen und Anwendungen
Regelmäßige Wartungsarbeiten zur Vorbeugung von Ausfällen
Ersetzen und Aufrüsten von Hardware-Komponenten
Aufgabenstellung
Ich hätte gern ein modernes Design. Ein Logo vorhanden, sollte mit eingebaut werden.
Ansonsten hätte ich gerne eine einzelne Webseite mit den Firmen Infos (und den Links zu Sozial Media) und einer extra Impressum Seite. Und wenn möglich noch ein Anfrage Formular.
Am liebsten wäre ein Format welches ich in WordPress verarbeiten werden kann.
(Logo wird noch nachgereicht)

```html
<!DOCTYPE html>
<html lang="de">
<head>
<meta charset="utf-8">
<title>Veltrano IT-Service Webdesign</title>
<link href="https://fonts.googleapis.com/css2?family=Inter:wght@400;500;600&display=swap" rel="stylesheet">
<style>
:root{
  --bg-dark:#262e34;
  --bg-green:#52705f;
  --panel:#ffffff;
  --hero:#2b3238;
  --ink:#22292e;
  --muted:#7c868b;
  --line:#c9d0d2;
  --teal:#6cc2b5;
  --teal-dark:#3f9d90;
  --mint:#eef5f2;
  --mint-2:#e3efea;
  --pill-dark:#2c3a40;
}
*{box-sizing:border-box;margin:0;padding:0}
html,body{width:1200px;height:900px;overflow:hidden}
body{font-family:"Inter",sans-serif;color:var(--ink);
  background:linear-gradient(100deg,var(--bg-dark) 0%,#303a3f 45%,#3e5550 80%,var(--bg-green) 100%);position:relative}
.abs{position:absolute}
.tiny{font-size:7px;color:var(--muted);line-height:11px}
.lines span{display:block}

/* right page */
.page-right{left:738px;top:0;width:424px;height:900px;background:var(--panel)}
.thumb{top:0;height:84px;border-radius:0 0 8px 8px;background:linear-gradient(135deg,#9aa1a4,#d6dadb)}
.r-title{font-size:14px;font-weight:400;color:#2c3337}
.btn-dark{background:var(--pill-dark);color:#fff;border-radius:12px;font-size:7px;display:flex;align-items:center;justify-content:center}
.icon-item{width:90px;text-align:left}
.icon-item svg{display:block;margin-bottom:8px}
.mint-zone{left:0;top:448px;width:424px;height:452px;background:linear-gradient(180deg,var(--mint) 0%,#f3f8f6 40%,var(--mint-2) 100%)}
.field{height:21px;border-radius:11px;background:#e2ede8;font-size:7px;color:#55666a;display:flex;align-items:center;padding-left:10px;gap:6px}
.white-card{background:#fff;border-radius:6px}
.band{left:0;top:660px;width:424px;height:70px;background:#e3eeea}

/* left page */
.page-left{left:40px;top:42px;width:710px;height:858px;background:var(--panel);border-radius:12px 12px 0 0;overflow:hidden}
.topbar{left:0;top:0;width:100%;height:20px}
.nav a{font-size:7px;color:#444c50;text-decoration:none;margin-right:26px}
.logo{font-size:13px;font-weight:600;color:var(--ink);display:flex;align-items:center;gap:6px}
.logo i{width:12px;height:12px;border:2px solid var(--teal-dark);border-radius:3px;display:block}
.btn-teal{background:var(--teal);color:#fff;border-radius:12px;font-size:7px;display:flex;align-items:center;justify-content:center}
.hero{left:5px;top:66px;width:700px;height:350px;border-radius:14px;overflow:hidden;
  background:linear-gradient(100deg,#2a3137 0%,#2e363b 60%,#33434a 100%)}
.hero-art{right:0;top:80px;width:260px;height:270px;
  background:radial-gradient(circle at 60% 55%,rgba(108,194,181,.45),rgba(108,194,181,.12) 45%,rgba(43,50,56,0) 70%)}
.hero h1{font-size:23px;font-weight:400;line-height:31px;color:#fff}
.hero .tiny{color:#c8cfd1}
.ghost{border:1px solid #4c565b;background:#363f44;color:#dfe4e5;border-radius:12px;font-size:7px;display:flex;align-items:center;justify-content:center}
.form-card{left:391px;top:44px;width:205px;height:238px;background:#fff;border-radius:6px;padding:14px}
.form-card h3{font-size:9.5px;font-weight:600;padding-bottom:6px;border-bottom:1px solid var(--line);margin-bottom:8px}
.form-row{height:19px;border-radius:10px;background:#f1f4f4;font-size:7px;color:#3c4549;display:flex;align-items:center;gap:6px;padding-left:8px;margin-bottom:10px}
.form-row b{width:7px;height:7px;border-radius:50%;border:1.5px solid var(--teal-dark)}
.section-tag{font-size:7px;color:var(--teal-dark);text-align:center}
.section-title{font-size:16px;line-height:23px;font-weight:400;text-align:center;color:#2b3236}
.card-img{top:646px;width:180px;height:94px;border-radius:4px}
.card-title{top:764px;font-size:14.5px;font-weight:400;color:#262d31}
.card-text{top:790px;width:180px}
</style>
</head>
<body>

<!-- right page: secondary screen -->
<div class="abs page-right">
  <div class="abs thumb" style="left:69px;width:139px" role="img" aria-label="Nahaufnahme einer Platine"></div>
  <div class="abs thumb" style="left:214px;width:139px" role="img" aria-label="Nahaufnahme von Hardware-Bauteilen"></div>

  <div class="abs r-title" style="left:69px;top:98px">Bereit für verlässliche IT-Partner</div>
  <div class="abs tiny lines" style="left:69px;top:124px;width:280px">
    <span>Seit 1997 betreuen wir Firmen und Privatkunden in Mainz mit Rat,</span>
    <span>schneller Hilfe und moderner Technik für Hardware und Software</span>
    <span>direkt vor Ort und aus der Ferne, persönlich und zuverlässig.</span>
    <span>Rufen Sie uns einfach an.</span>
  </div>

  <div class="abs" style="left:69px;top:215px;width:62px;height:1px;background:var(--teal-dark)"></div>
  <div class="abs" style="left:69px;top:230px;width:16px;height:1px;background:#333"></div>
  <div class="abs" style="left:69px;top:244px;width:16px;height:1px;background:#333"></div>
  <div class="abs r-title" style="left:140px;top:210px">System-Wartung</div>
  <div class="abs tiny lines" style="left:140px;top:230px;width:220px">
    <span>Regelmäßige Pflege beugt Ausfällen vor und hält Ihre</span>
    <span>Systeme schnell, sicher und auf aktuellem Stand.</span>
  </div>
  <div class="abs btn-dark" style="left:139px;top:262px;width:74px;height:20px">Termin anfragen</div>

  <div class="abs icon-item tiny" style="left:69px;top:345px">
    <svg width="18" height="16" viewBox="0 0 18 16" fill="none" stroke="#3f9d90" stroke-width="1.4"><path d="M2 2h10v5H4v6h12"/></svg>
    <span style="display:block">Beratung &amp; Analyse</span><span style="display:block">vor Ort</span>
  </div>
  <div class="abs icon-item tiny" style="left:172px;top:345px">
    <svg width="18" height="16" viewBox="0 0 18 16" fill="none" stroke="#3f9d90" stroke-width="1.4"><rect x="2" y="2" width="14" height="12" rx="2"/><path d="M6 8h6M9 5v6"/></svg>
    Schnelle Reparatur
  </div>
  <div class="abs icon-item tiny" style="left:275px;top:345px">
    <svg width="18" height="16" viewBox="0 0 18 16" fill="none" stroke="#3f9d90" stroke-width="1.4"><circle cx="7" cy="7" r="4"/><circle cx="12" cy="10" r="3"/></svg>
    Daten gesichert
  </div>

  <div class="abs mint-zone"></div>
  <div class="abs r-title" style="left:34px;top:458px">Impressum</div>
  <div class="abs field" style="left:38px;top:484px;width:122px">
    <svg width="8" height="8" viewBox="0 0 8 8" fill="none" stroke="#3f9d90" stroke-width="1.2"><circle cx="3.5" cy="3.5" r="2.5"/><path d="M5.5 5.5L7.5 7.5"/></svg>Name und Firma
  </div>
  <div class="abs field" style="left:168px;top:484px;width:122px">
    <svg width="8" height="8" viewBox="0 0 8 8" fill="none" stroke="#3f9d90" stroke-width="1.2"><rect x="1" y="1" width="6" height="6" rx="1"/></svg>E-Mail Adresse
  </div>
  <div class="abs" style="left:296px;top:484px;width:21px;height:21px;border-radius:50%;background:#e2ede8">
    <svg width="21" height="21" viewBox="0 0 21 21" fill="none" stroke="#3f9d90" stroke-width="1.4"><path d="M9 7l3.5 3.5L9 14"/></svg>
  </div>
  <div class="abs white-card" style="left:34px;top:537px;width:290px;height:100px;padding:14px 12px">
    <div style="font-size:7px;font-weight:600;margin-bottom:8px">Angaben gemäß § 5 TMG</div>
    <div class="tiny lines" style="color:#4a5357">
      <span>Veltrano IT-Service, Inhaber und Ansprechpartner vor Ort,</span>
      <span>Musterstraße 12, 55116 Mainz, Telefon und Kontakt siehe</span>
      <span>unten, Umsatzsteuer-ID auf Anfrage erhältlich.</span>
      <span>Stand 2024</span>
    </div>
  </div>

  <div class="abs band"></div>
  <div class="abs" style="left:38px;top:676px;display:flex;gap:8px">
    <svg width="26" height="20" viewBox="0 0 26 20" fill="none" stroke="#3f9d90" stroke-width="1.4"><rect x="2" y="2" width="20" height="13" rx="1"/><path d="M8 18h8"/></svg>
    <div class="tiny" style="color:#3c4549"><b style="font-weight:600">Fernwartung</b><br>Hilfe schnell und direkt per Netz</div>
  </div>
  <div class="abs" style="left:192px;top:676px;display:flex;gap:8px">
    <svg width="26" height="20" viewBox="0 0 26 20" fill="none" stroke="#3f9d90" stroke-width="1.4"><circle cx="12" cy="6" r="4"/><path d="M3 18c2-5 16-5 18 0"/></svg>
    <div class="tiny" style="color:#3c4549"><b style="font-weight:600">Vor-Ort-Service</b><br>Wir kommen zu Ihnen ins Haus</div>
  </div>

  <div class="abs white-card" style="left:34px;top:735px;width:356px;height:170px;padding:18px 32px;border-radius:8px">
    <div class="r-title" style="margin-bottom:14px">Impressum</div>
    <div class="tiny lines" style="color:#4a5357;margin-bottom:8px">
      <span>Verantwortlich für den Inhalt dieser Seite ist der Inhaber von Veltrano</span>
      <span>IT-Service. Trotz sorgfältiger Kontrolle übernehmen wir keine Haftung</span>
      <span>für Inhalte externer Links. Für diese sind ausschließlich deren Betreiber</span>
      <span>verantwortlich. Alle Angaben ohne Gewähr und vorbehaltlich Änderungen.</span>
    </div>
    <div class="tiny lines" style="color:#4a5357">
      <span>Streitschlichtung: Wir sind nicht verpflichtet und nicht bereit, an einem</span>
      <span>Streitbeilegungsverfahren vor einer Verbraucherschlichtungsstelle</span>
      <span>teilzunehmen. Kontakt jederzeit gern.</span>
    </div>
    <div style="display:flex;gap:4px;margin-top:12px">
      <svg width="26" height="20" viewBox="0 0 26 20" fill="none" stroke="#3f9d90" stroke-width="1.4"><rect x="1" y="1" width="24" height="18" rx="9"/><path d="M14 6l-4 4 4 4"/></svg>
      <svg width="26" height="20" viewBox="0 0 26 20" fill="none" stroke="#2c3a40" stroke-width="1.4"><rect x="1" y="1" width="24" height="18" rx="9"/><path d="M11 6l4 4-4 4"/></svg>
    </div>
  </div>
</div>

<!-- left page: main screen -->
<div class="abs page-left">
  <div class="abs topbar">
    <svg class="abs" style="left:72px;top:6px" width="10" height="8" viewBox="0 0 10 8" fill="none" stroke="#3f9d90" stroke-width="1.4"><path d="M1 1h8M1 4h5M1 7h8"/></svg>
    <div class="abs tiny" style="left:88px;top:5px;color:#555">Seit 1997, Mainz, IT-Service</div>
    <div class="abs tiny" style="left:547px;top:5px;color:#555">Kontakt</div>
    <div class="abs" style="left:611px;top:6px;width:8px;height:8px;border-radius:50%;border:1.5px solid var(--teal-dark)"></div>
    <div class="abs" style="left:629px;top:6px;width:6px;height:8px;border-right:1.5px solid var(--teal-dark);border-radius:0 6px 6px 0"></div>
  </div>
  <div class="abs" style="left:0;top:21px;width:100%;height:1px;background:#eef0f0"></div>

  <div class="abs logo" style="left:72px;top:33px"><i></i>Veltrano</div>
  <div class="abs nav" style="left:220px;top:37px">
    <a>Home</a><a>Services</a><a>Über uns Infos</a><a>Anfrage Form</a><a>Social Links</a>
  </div>
  <div class="abs btn-teal" style="left:564px;top:32px;width:74px;height:22px">Jetzt anfragen</div>

  <div class="abs hero">
    <div class="abs hero-art" role="img" aria-label="Leuchtendes Netzwerk aus verbundenen Linien und Punkten"></div>
    <div class="abs tiny" style="left:60px;top:78px">Seit 1997 ✓</div>
    <h1 class="abs" style="left:60px;top:94px;width:330px">Diagnosing IT Services<br>System Optimizing,<br>Hardware Upgrades</h1>
    <div class="abs tiny lines" style="left:60px;top:204px;width:290px">
      <span>Computer-Service Mainz für Firmen und Privatkunden, kompetent</span>
      <span>beraten und zuverlässig betreut, von Fehlerdiagnose bis Wartung</span>
      <span>alles aus einer Hand.</span>
    </div>
    <div class="abs btn-teal" style="left:60px;top:257px;width:72px;height:24px">Mehr erfahren</div>
    <div class="abs ghost" style="left:143px;top:257px;width:92px;height:24px">Unsere Leistungen</div>
    <div class="abs ghost" style="left:240px;top:257px;width:24px;height:24px;border-radius:50%">
      <svg width="10" height="10" viewBox="0 0 10 10" fill="none" stroke="#dfe4e5" stroke-width="1.2"><circle cx="5" cy="5" r="4"/><path d="M5 3v2l1.5 1"/></svg>
    </div>

    <div class="abs form-card">
      <h3>Das Service-Anfrage-Formular</h3>
      <div class="form-row"><b></b>Ihr Name</div>
      <div class="form-row"><b></b>E-Mail</div>
      <div class="form-row"><b></b>Telefon</div>
      <div class="form-row"><b></b>Gerät</div>
      <div class="form-row"><b></b>Ihr Anliegen</div>
      <div class="btn-teal" style="height:24px;margin-top:10px">Anfrage senden</div>
    </div>
  </div>

  <div class="abs section-tag" style="left:0;top:455px;width:710px">Computer-Service</div>
  <div class="abs section-title" style="left:0;top:470px;width:710px">IT-Dienstleistungen und Computer-Service<br>Mainz: Wartung und Beratung</div>
  <div class="abs tiny lines" style="left:155px;top:526px;width:400px;text-align:center">
    <span>Wir optimieren und erhalten Ihre IT-Infrastruktur, von der Fehlerdiagnose</span>
    <span>bis zur Wartung bieten wir ein Rundum-Sorglos-Paket für Hardware und</span>
    <span>Software in Mainz und Umgebung.</span>
  </div>
  <div class="abs btn-dark" style="left:299px;top:571px;width:76px;height:23px">Alle Services</div>

  <div class="abs card-img" style="left:73px;background:linear-gradient(135deg,#c9ccc9,#e6e7e4)" role="img" aria-label="Foto eines Technikers im Büro"></div>
  <div class="abs card-img" style="left:265px;background:linear-gradient(135deg,#3e4447,#a4a9a8)" role="img" aria-label="Foto eines Monitors am Arbeitsplatz"></div>
  <div class="abs card-img" style="left:457px;background:linear-gradient(135deg,#dfe1e2,#3f5fbf 70%,#2b3a80)" role="img" aria-label="Foto eines Laptops mit blauem Bildschirm"></div>

  <div class="abs card-title" style="left:73px">Fehleranalyse</div>
  <div class="abs card-title" style="left:265px">Reparatur &amp; Hilfe</div>
  <div class="abs card-title" style="left:457px">System-Optimierung</div>

  <div class="abs tiny lines card-text" style="left:73px">
    <span>Professionelle Fehleranalyse und</span><span>schnelle Reparatur für Ihre Rechner</span>
    <span>und Netzwerke, direkt vor Ort oder</span><span>in unserer Werkstatt mit klarer</span>
    <span>Auskunft zu Kosten und Dauer.</span>
  </div>
  <div class="abs tiny lines card-text" style="left:265px">
    <span>Regelmäßige Wartungsarbeiten zur</span><span>Vorbeugung von Ausfällen halten</span>
    <span>Ihre Geräte leistungsfähig, sicher</span><span>und stets aktuell im Alltag für</span>
    <span>Büro und Zuhause.</span>
  </div>
  <div class="abs tiny lines card-text" style="left:457px">
    <span>Optimierung von Betriebssystemen</span><span>und Anwendungen sowie Ersetzen</span>
    <span>und Aufrüsten von Hardware für</span><span>mehr Tempo und eine lange Lebens-</span>
    <span>dauer.</span>
  </div>
</div>

</body>
</html>
```